Corvana Teal Outings is an Exciting Water and Land Excursions business that needs a website.

We need a website for our company. We are based in Bimini Bahamas and we sell land and sea excursions. We sell Private boat Charters, Reef Shark Snorkeling, Merloth Shipwreck Snorkeling, Stingray feeding adventures, Dolphin Tours, Sunset Cruises, Scuba Diving, Offshore Fishing, Reef Fishing, Flats Backwater Fishing, Party Island Cruise, Island Land Party Bicycle Tours, Jet Ski Tours, Guided Kayak Tours, Beach Chairs/Umbrella Rentals, Cabana Rentals, Jet Ski Rentals, Kayak Rentals, Paddle Board Rentals, Water Hammock Rentals, and Paint by the Sea Excursion

The home page will have the following tabs:
Adventures
Watersports
Photos
Alcohol
START YOUR ADVENTURE - Booking button
The adventures

We are currently using tallvex for our reservation system and that will need to be integrated with our website along with quarmona or a similar app for purchase of photos.
Updates

Need extra days to review

Target Market(s)

Our target market are tourists

Industry/Entity Type

Tourism

Coding

Coded - Design and coding required

Font styles to use
Sans Serif

Colors
0094D4
00A9DD
6FCCEA
C7EBF8
E9F6FB

Requirements
Must have
• The website must be in wordpress so we can add our external reservation system
Nice to have
• We need to have big photos and a lot of photos

```html
<!DOCTYPE html>
<html lang="en">
<head>
<meta charset="utf-8">
<title>Corvana Teal Outings</title>
<link href="https://fonts.googleapis.com/css2?family=Poppins:wght@400;500;600;700;800&display=swap" rel="stylesheet">
<style>
:root{
  --blue:#0094D4;
  --blue-2:#00A9DD;
  --sky:#6FCCEA;
  --pale:#C7EBF8;
  --mist:#E9F6FB;
  --nav:#1a86d4;
  --navy:#0d2a4a;
  --ink:#111;
  --body:#555;
  --btn:#3aa9e4;
}
*{margin:0;padding:0;box-sizing:border-box}
html,body{width:1200px;height:4577px;overflow:hidden}
body{font-family:"Poppins",sans-serif;color:var(--ink);background:#fff;position:relative}
.abs{position:absolute}
.btn{position:absolute;display:flex;align-items:center;justify-content:center;background:var(--btn);color:#fff;font-weight:600;font-size:17px;letter-spacing:.5px;border-radius:40px;text-transform:uppercase}
.ph{position:absolute}

/* header */
.topbar{position:absolute;left:0;top:0;width:1200px;height:128px;background:var(--mist)}
.brand{position:absolute;left:75px;top:30px;display:flex;align-items:center;gap:10px}
.brand-dot{width:44px;height:44px;border-radius:50%;background:#1b8a4a}
.brand-name{font-weight:700;font-size:17px;color:var(--navy);line-height:1.1;width:120px}
.phone{position:absolute;left:515px;top:46px;display:flex;align-items:center;gap:10px;font-weight:600;font-size:22px;color:var(--navy)}
.nav{position:absolute;left:0;top:128px;width:1200px;height:68px;background:var(--nav);display:flex;padding-left:75px}
.nav a{color:#fff;font-weight:600;font-size:15px;text-transform:uppercase;display:flex;align-items:center;padding:0 26px;text-decoration:none}
.nav a.active{background:var(--sky);width:128px;justify-content:center;padding:0}

/* hero */
.hero{position:absolute;left:0;top:196px;width:1200px;height:657px;background:linear-gradient(180deg,#3b5663 0%,#1f4a5a 40%,#1a4256 75%,#23465a 100%)}
.hero h1{position:absolute;top:120px;width:100%;text-align:center;color:#fff;font-size:92px;font-weight:800;letter-spacing:1px}
.hero p{position:absolute;top:236px;width:100%;text-align:center;color:#fff;font-size:31px;font-weight:700;line-height:40px}
.dots{position:absolute;top:518px;left:482px;display:flex;gap:16px}
.dots span{width:48px;height:4px;background:var(--blue-2)}
.dots span:first-child{background:#fff}

/* welcome */
.section-title{font-weight:700;color:var(--blue);font-size:50px;letter-spacing:1px;line-height:1}
.para{font-size:16px;line-height:33px;color:var(--body)}

/* split */
.split-title{position:absolute;color:#fff;font-size:50px;font-weight:700;width:600px;text-align:center}
.split-text{position:absolute;color:#fff;font-size:16px;line-height:30px;width:600px;text-align:center}

.photos{position:absolute;left:0;top:3413px;width:1200px;height:672px;background:var(--mist)}
.photos h2{position:absolute;top:65px;width:100%;text-align:center;font-size:36px;font-weight:700}

.reserve{position:absolute;left:0;top:4085px;width:1200px;height:315px;background:linear-gradient(180deg,#1565a8,#0f5b98 60%,#1a6aa8)}
.reserve h2{position:absolute;top:48px;width:100%;text-align:center;color:#fff;font-size:36px;font-weight:700}
.reserve p{position:absolute;top:112px;width:100%;text-align:center;color:#fff;font-size:16px;line-height:34px}

.footer-nav{position:absolute;top:4440px;left:0;width:1200px;display:flex;justify-content:center;gap:45px}
.footer-nav a{font-size:15px;font-weight:600;color:#111;text-decoration:none;text-transform:uppercase}
.copy{position:absolute;top:4482px;width:1200px;text-align:center;font-size:14px;color:#333}
.social{position:absolute;top:4518px;left:504px;display:flex;gap:20px}
.social span{width:22px;height:22px;border-radius:50%;background:#555}
</style>
</head>
<body>

<header class="topbar">
  <div class="brand"><span class="brand-dot"></span><span class="brand-name">CORVANA TEAL OUTINGS</span></div>
  <div class="phone">
    <svg width="20" height="22" viewBox="0 0 24 24"><path d="M6.6 10.8a15 15 0 0 0 6.6 6.6l2.2-2.2a1 1 0 0 1 1-.25 11 11 0 0 0 3.6.6 1 1 0 0 1 1 1V20a1 1 0 0 1-1 1A17 17 0 0 1 3 4a1 1 0 0 1 1-1h3.5a1 1 0 0 1 1 1 11 11 0 0 0 .6 3.6 1 1 0 0 1-.25 1z" fill="#2b9be0"/></svg>
    +1-800-555-0142
  </div>
  <a class="btn" style="left:795px;top:34px;width:330px;height:58px">Start your adventure</a>
</header>

<nav class="nav">
  <a class="active">Home</a><a>Adventures</a><a>Watersports</a><a>Photos</a><a>Alcohol</a><a>The Adventures</a><a>Contact us</a>
</nav>

<section class="hero" role="img" aria-label="Aerial view of marina docks and turquoise sea">
  <h1>CORVANA TEAL</h1>
  <p>Corvana Teal Outings is an Exciting Water and<br>Land Excursions business.</p>
  <a class="btn" style="left:434px;top:343px;width:332px;height:57px">Start your adventure</a>
  <div class="dots"><span></span><span></span><span></span><span></span></div>
  <svg class="abs" style="left:0;bottom:0" width="1200" height="100" viewBox="0 0 1200 100" preserveAspectRatio="none">
    <path d="M0 100 L0 80 C150 0 330 20 520 45 C700 70 830 40 960 20 C1060 5 1140 15 1200 30 L1200 100 Z" fill="#fff"/>
  </svg>
</section>

<section>
  <div class="ph" style="left:75px;top:928px;width:249px;height:203px;background:linear-gradient(135deg,#2a3350,#5a6f8a)" role="img" aria-label="Party bicycle bus lit with neon lights"></div>
  <div class="ph" style="left:338px;top:928px;width:249px;height:203px;background:linear-gradient(180deg,#8fb7d6,#c9d3d8)" role="img" aria-label="Beach cabana with ocean view"></div>
  <div class="ph" style="left:75px;top:1145px;width:512px;height:220px;background:linear-gradient(180deg,#9cc3e4,#5ea3a8 55%,#8d8a7d)" role="img" aria-label="Turquoise beach house with outdoor tables"></div>
  <div class="abs" style="left:615px;top:930px;font-size:36px;font-weight:700;line-height:1">WELCOME TO</div>
  <div class="abs section-title" style="left:615px;top:968px;font-size:56px">CORVANA TEAL</div>
  <p class="abs para" style="left:615px;top:1040px;width:520px">Sed ut perspiciatis unde omnis iste natus error sit voluptatem accusantium doloremque laudantium, totam rem aperiam, eaque ipsa quae ab illo inventore veritatis et quasi architecto beatae vitae dicta sunt explicabo. Nemo enim ipsam voluptatem quia voluptas sit aspernatur aut odit aut fugit, sed quia consequuntur magni dolores eos qui ratione voluptatem sequi nesciunt.</p>
  <a class="btn" style="left:615px;top:1300px;width:194px;height:57px">Read more</a>
</section>

<section class="abs" style="left:0;top:1445px;width:1200px;height:480px">
  <svg class="abs" style="left:0;top:0" width="1200" height="480" role="img" aria-label="Beach with umbrellas and docked boats at a marina">
    <defs>
      <linearGradient id="gSell" x1="0" y1="0" x2="0" y2="1"><stop offset="0" stop-color="#3f5a5a"/><stop offset=".5" stop-color="#24505a"/><stop offset="1" stop-color="#163e4c"/></linearGradient>
      <linearGradient id="gRent" x1="0" y1="0" x2="0" y2="1"><stop offset="0" stop-color="#1d5a98"/><stop offset=".5" stop-color="#174e86"/><stop offset="1" stop-color="#1f5f96"/></linearGradient>
    </defs>
    <polygon points="0,0 635,0 572,480 0,480" fill="url(#gSell)"/>
    <polygon points="635,0 1200,0 1200,480 572,480" fill="url(#gRent)"/>
  </svg>
  <div class="split-title" style="left:-10px;top:136px">SELL</div>
  <div class="split-text" style="left:-10px;top:200px">Sed ut perspiciatis unde omnis iste natus error sit<br>voluptatem accusantium doloremque</div>
  <a class="btn" style="left:194px;top:279px;width:194px;height:57px">Read more</a>
  <div class="split-title" style="left:587px;top:136px">RENT</div>
  <div class="split-text" style="left:587px;top:200px">Sed ut perspiciatis unde omnis iste natus error sit<br>voluptatem accusantium doloremque</div>
  <a class="btn" style="left:790px;top:279px;width:194px;height:57px">Read more</a>
</section>

<section>
  <div class="ph" style="left:75px;top:1986px;width:526px;height:451px;background:linear-gradient(180deg,#6f99c8,#b9c9d8 50%,#5a6a72)" role="img" aria-label="Excursion boat moored at a dock"></div>
  <div class="abs section-title" style="left:638px;top:2040px;font-size:46px">ADVENTURES</div>
  <p class="abs para" style="left:638px;top:2102px;width:490px">Sed ut perspiciatis unde omnis iste natus error sit voluptatem accusantium doloremque laudantium, totam rem aperiam, eaque ipsa quae ab illo inventore veritatis et quasi architecto beatae vitae dicta sunt explicabo. Nemo enim ipsam voluptatem quia voluptas sit aspernatur aut odit aut fugit, sed quia consequuntur.</p>
  <a class="btn" style="left:638px;top:2319px;width:194px;height:57px">Read more</a>

  <div class="abs section-title" style="left:75px;top:2493px;font-size:46px">WATERSPORTS</div>
  <p class="abs para" style="left:75px;top:2555px;width:490px">Sed ut perspiciatis unde omnis iste natus error sit voluptatem accusantium doloremque laudantium, totam rem aperiam, eaque ipsa quae ab illo inventore veritatis et quasi architecto beatae vitae dicta sunt explicabo. Nemo enim ipsam voluptatem quia voluptas sit aspernatur aut odit aut fugit, sed quia consequuntur.</p>
  <a class="btn" style="left:75px;top:2772px;width:194px;height:57px">Read more</a>
  <div class="ph" style="left:601px;top:2437px;width:524px;height:454px;background:linear-gradient(180deg,#5b8fc9,#4aa3b4 45%,#d8cfbd 65%,#e6dccb)" role="img" aria-label="Kayaks and paddle boards on a sandy beach"></div>

  <div class="ph" style="left:75px;top:2891px;width:526px;height:453px;background:linear-gradient(160deg,#3e2a22,#b06a3a 50%,#e8a060 70%,#5a3a2a)" role="img" aria-label="Two wine glasses toasting at sunset"></div>
  <div class="abs section-title" style="left:638px;top:2946px;font-size:46px">ALCOHOL</div>
  <p class="abs para" style="left:638px;top:3008px;width:490px">Sed ut perspiciatis unde omnis iste natus error sit voluptatem accusantium doloremque laudantium, totam rem aperiam, eaque ipsa quae ab illo inventore veritatis et quasi architecto beatae vitae dicta sunt explicabo. Nemo enim ipsam voluptatem quia voluptas sit aspernatur aut odit aut fugit, sed quia consequuntur.</p>
  <a class="btn" style="left:638px;top:3225px;width:194px;height:57px">Read more</a>
</section>

<section class="photos">
  <h2>PHOTOS</h2>
  <div class="ph" style="left:75px;top:146px;width:334px;height:221px;background:linear-gradient(180deg,#8db4d8,#3e6f9a)" role="img" aria-label="Speedboat on open water"></div>
  <div class="ph" style="left:75px;top:381px;width:334px;height:220px;background:linear-gradient(180deg,#6f8da8,#3a5d7a)" role="img" aria-label="Excursion boat under cloudy sky"></div>
  <div class="ph" style="left:425px;top:146px;width:352px;height:455px;background:linear-gradient(180deg,#2f7fb8,#3fa2c2 45%,#d6cbb6 70%,#c85040)" role="img" aria-label="Guides with jet skis and kayaks on the beach"></div>
  <div class="ph" style="left:791px;top:146px;width:334px;height:221px;background:linear-gradient(180deg,#6fa7d8,#2d9ab8)" role="img" aria-label="Snorkelers near an old pier"></div>
  <div class="ph" style="left:791px;top:381px;width:334px;height:220px;background:linear-gradient(180deg,#8fb6d2,#5a8aa0 60%,#9a9a90)" role="img" aria-label="Wooden dock with boats"></div>
</section>

<section class="reserve" role="img" aria-label="Aerial view of beach with umbrellas">
  <h2>MAKE A RESERVATION</h2>
  <p>Sed ut perspiciatis unde omnis iste natus error sit voluptatem accusantium doloremque laudantium,<br>totam rem aperiam, eaque ipsa quae ab illo inventore veritatis.</p>
  <a class="btn" style="left:452px;top:201px;width:295px;height:56px">Start your adventure</a>
</section>

<footer>
  <nav class="footer-nav"><a>Home</a><a>Adventures</a><a>Watersports</a><a>Photos</a><a>Alcohol</a><a>The Adventures</a><a>Contact us</a></nav>
  <div class="copy">Copyright © 2022. Company Name All rights reserved.</div>
  <div class="social"><span></span><span></span><span></span><span></span><span></span></div>
</footer>

</body>
</html>
```